Web Design for Financial Consulting Company

We need a website design for a financial consulting company "Kelvane Consulting". We build financial models, scenario analysis, handle the budgeting process and provide temporary staffing. I have over 10 years of experience. My Excel expertise and analytical savvy has saved clients over $17 million in profit.

Target Market(s)

Small to medium businesses

Industry/Entity Type

Financial Consulting

Number of Pages Required

4 page

Requirements
Must have
• Professional looking
Nice to have
• A little futuristic looking

```html
<!DOCTYPE html>
<html lang="en">
<head>
<meta charset="utf-8">
<title>Kelvane Consulting</title>
<link href="https://fonts.googleapis.com/css2?family=Outfit:wght@400;500;600;700&family=Montserrat:wght@400;500;600&display=swap" rel="stylesheet">
<style>
:root{
  --blue:#12a4ee;
  --navy:#0b1d33;
  --footer:#0d3360;
  --ink:#1b2430;
  --muted:#7b8590;
  --light:#f4f8fc;
  --white:#ffffff;
}
*{margin:0;padding:0;box-sizing:border-box}
html,body{width:1200px;height:3402px;overflow:hidden}
body{position:relative;background:var(--white);font-family:"Montserrat",sans-serif;color:var(--ink)}
.abs{position:absolute}
h1,h2,h3,.head{font-family:"Outfit",sans-serif}
.btn{position:absolute;background:var(--blue);color:var(--white);font-family:"Outfit",sans-serif;font-size:15px;font-weight:500;display:flex;align-items:center;justify-content:center}
.eyebrow{position:absolute;color:var(--blue);font-family:"Outfit",sans-serif;font-size:13px;font-weight:600;text-transform:uppercase}
.rule{position:absolute;height:1px;width:40px;background:#cfd6dd}

/* header & hero */
.hero-photo{left:0;top:0;width:1200px;height:660px;background:radial-gradient(circle at 1090px 160px,#f3b270 0,#9c6e4a 40px,transparent 110px),radial-gradient(ellipse at 750px 400px,#1d6aa8 0,#0e3356 260px,transparent 480px),linear-gradient(100deg,#070f1c 0%,#0b1d33 45%,#12385e 100%)}
.wedge{left:0;top:480px}
.logo{display:flex;align-items:center;gap:10px;color:var(--white)}
.logo .mark{width:30px;height:30px;border:4px solid var(--blue)}
.logo .name{font-family:"Outfit",sans-serif;font-weight:700;font-size:24px;letter-spacing:1px;line-height:1}
.site-logo{left:161px;top:18px}
.nav a{position:absolute;top:27px;font-family:"Outfit",sans-serif;font-size:15px;color:var(--white);text-decoration:none}
.nav .active{color:var(--blue)}
.hero-title{left:161px;top:172px;width:460px;color:var(--white);font-size:45px;font-weight:600;line-height:58px;white-space:nowrap}

/* about */
.about-mark{left:90px;top:700px;width:167px;height:167px;border:10px solid var(--blue)}
.photo-laptop{left:276px;top:682px;width:313px;height:264px;background:linear-gradient(135deg,#d9dee3,#a9b3bc 60%,#6f7a86)}
.photo-calc{left:169px;top:887px;width:199px;height:180px;background:linear-gradient(135deg,#7c8793,#c8ced5 55%,#e4e7ea)}
.years{left:393px;top:958px;font-family:"Outfit",sans-serif;color:var(--ink);font-size:34px;font-weight:500}
.years b{color:var(--blue);font-size:60px;font-weight:500}
.years-sub{left:403px;top:1033px;color:var(--blue);font-size:15px;letter-spacing:4px}
.about-title{left:624px;top:738px;font-size:30px;font-weight:500}
.about-lead{left:624px;top:800px;width:410px;font-size:12px;font-weight:500;line-height:24.5px}
.about-body{left:624px;top:905px;width:410px;font-size:12px;color:var(--muted);line-height:24.5px}

/* services */
.services-bg{left:0;top:1135px;width:1200px;height:620px;background:var(--light)}
.sec-title{font-size:30px;font-weight:500}
.services-intro{left:479px;top:1206px;width:560px}
.services-intro h3{font-size:15px;font-weight:500;margin-bottom:10px}
.services-intro p{font-size:12px;color:#5c6670;line-height:24.5px}
.service-card{position:absolute;top:1340px;width:277px;height:317px;background:var(--white);border-bottom:4px solid var(--blue)}
.service-card svg{position:absolute;left:68px;top:28px}
.service-card .num{position:absolute;left:20px;top:97px;font-family:"Outfit",sans-serif;color:var(--blue);font-size:24px}
.service-card h3{position:absolute;left:70px;top:100px;font-size:17px;font-weight:500;line-height:20px}
.service-card p{position:absolute;left:70px;top:153px;width:190px;font-size:12px;color:var(--muted);line-height:24.5px}
.arrow{position:absolute;font-size:26px;line-height:1}

/* reviews */
.center{text-align:center;left:0;width:1200px}
.review-card{position:absolute;width:277px;height:261px;background:var(--white);box-shadow:0 6px 22px rgba(20,50,90,.08);overflow:hidden}
.avatar{position:absolute;left:20px;top:22px;width:58px;height:58px;border-radius:50%;background:linear-gradient(135deg,#4c6580,#b9c4cf)}
.quote{position:absolute;right:28px;top:18px;font-family:"Outfit",sans-serif;font-size:60px;color:#d4eefb;line-height:1}
.review-card p{position:absolute;left:20px;top:104px;width:240px;font-size:12px;line-height:20px;color:var(--ink)}
.review-card .by{position:absolute;left:20px;top:204px;font-size:12px;font-weight:600}
.stars{position:absolute;left:28px;top:222px;font-size:18px;color:#f5b21b;letter-spacing:1px}
.stars span{color:#c6c9cc}
.arrow-box{position:absolute;top:1898px;width:39px;height:39px;display:flex;align-items:center;justify-content:center;font-size:22px}

/* blogs */
.blogs-bg{left:0;top:2343px;width:1200px;height:673px;background:var(--light)}
.blog{position:absolute;top:2488px;width:278px}
.blog .img{height:201px}
.blog h3{margin-top:22px;font-size:15px;font-weight:500;line-height:24px}
.blog p{margin-top:5px;font-size:12px;line-height:20px;color:#4a545e}
.blog .author{display:flex;align-items:center;gap:14px;margin-top:14px}
.blog .author i{width:38px;height:38px;border-radius:50%;background:linear-gradient(135deg,#8d97a2,#d8dde2)}
.blog .author b{display:block;font-family:"Outfit",sans-serif;font-size:13px;font-weight:500}
.blog .author small{font-size:10px;color:var(--muted)}

/* footer */
.footer{left:0;top:3016px;width:1200px;height:386px;background:var(--footer);color:var(--white)}
.footer .logo .name{font-size:32px}
.footer .logo .mark{width:40px;height:40px}
.footer-about{left:161px;top:142px;width:280px;font-size:11px;line-height:20.5px}
.social{position:absolute;top:251px;width:37px;height:37px;border:1px solid rgba(255,255,255,.55)}
.fhead{position:absolute;top:116px;color:var(--blue);font-family:"Outfit",sans-serif;font-size:15px}
.fhead::before{content:"";display:inline-block;width:18px;height:1px;background:var(--blue);vertical-align:middle;margin-right:6px}
.fitem{position:absolute;font-size:11px;line-height:15px}
.subscribe-box{left:812px;top:195px;width:227px;height:30px;background:#0a2a50;font-size:10px;padding:10px 14px}
.send{left:1006px;top:180px;width:33px;height:32px;background:var(--blue);display:flex;align-items:center;justify-content:center}
.copy{left:0;top:347px;width:1200px;text-align:center;font-size:11px}
</style>
</head>
<body>

<!-- Header & hero -->
<div class="abs hero-photo" role="img" aria-label="Businessman touching a glowing finance growth chart with data overlays"></div>
<svg class="abs wedge" width="1200" height="180" viewBox="0 0 1200 180">
  <path d="M0 18 L869 170 L1200 35 L1200 180 L0 180 Z" fill="var(--blue)"/>
  <path d="M0 46 L869 170 L1200 35 L1200 180 L0 180 Z" fill="var(--white)"/>
</svg>
<div class="abs logo site-logo"><span class="mark"></span><span class="name">KELVANE</span></div>
<nav class="nav">
  <a class="active" style="left:602px">Home</a>
  <a style="left:693px">About Us</a>
  <a style="left:808px">Services</a>
</nav>
<div class="btn" style="left:916px;top:18px;width:123px;height:36px">Contact Us</div>
<h1 class="abs hero-title">Helping Your<br>Finance Team And<br>Increasing Profit</h1>
<div class="btn" style="left:161px;top:364px;width:121px;height:37px">Contact Us</div>

<!-- About -->
<div class="abs about-mark"></div>
<div class="abs photo-calc" role="img" aria-label="Hands working with a calculator and financial documents"></div>
<div class="abs photo-laptop" role="img" aria-label="Laptop showing financial charts on a desk with glasses"></div>
<div class="abs years"><b>10</b>Years</div>
<div class="abs years-sub">Of Experience</div>
<div class="eyebrow" style="left:624px;top:714px">About Us</div>
<h2 class="abs about-title">Who We Are</h2>
<div class="rule" style="left:624px;top:783px"></div>
<p class="abs about-lead">I am an experienced Finance professional who develops strategic financial plans, provides insightful analysis, and supports decision – making. With over 10 years of experience, I have successfully increased profitability for clients by $17M.</p>
<p class="abs about-body">Lorem ipsum dolor sit amet, consetetur sadipscing elitr, sed diam nonumy eirmod tempor invidunt ut labore et dolore magna aliquyam erat, sed diam voluptua.</p>
<div class="btn" style="left:624px;top:989px;width:113px;height:37px;font-size:14px">Read More</div>

<!-- Services -->
<div class="abs services-bg"></div>
<div class="eyebrow" style="left:199px;top:1220px">Our Services</div>
<h2 class="abs sec-title" style="left:199px;top:1236px">Financial Models</h2>
<div class="rule" style="left:199px;top:1284px"></div>
<div class="abs services-intro">
  <h3>Lorem ipsum dolor sit amet, consectetuer adipiscing elit</h3>
  <p>Lorem ipsum dolor sit amet, consetetur sadipscing elitr, sed diam nonumy eirmod tempor invidunt ut labore et dolore magna aliquyam erat, sed diam voluptua.orem ipsum dolor sit amet, consetetur sadipscing elitr, sed diam nonumy...</p>
</div>
<span class="arrow" style="left:105px;top:1484px">&larr;</span>
<span class="arrow" style="left:1074px;top:1484px;color:var(--blue)">&rarr;</span>

<div class="service-card" style="left:161px">
  <svg width="50" height="54" viewBox="0 0 50 54" fill="none" stroke="#1b2430" stroke-width="2"><rect x="4" y="4" width="28" height="40"/><path d="M10 14h16M10 22h10M10 30h8"/><circle cx="33" cy="35" r="9" stroke="var(--blue)"/><path d="M40 42l7 7"/></svg>
  <span class="num">01</span><h3>Scenario<br>Analysis</h3>
  <p>Lorem ipsum dolor sit amet, consetetur sadipscing elitr, sed diam nonumy eirmod tempor invidunt ut labore et dolore magna aliquyam erat...</p>
</div>
<div class="service-card" style="left:461px">
  <svg width="54" height="50" viewBox="0 0 54 50" fill="none" stroke="#1b2430" stroke-width="2"><circle cx="18" cy="28" r="11"/><circle cx="18" cy="28" r="4" stroke="var(--blue)"/><circle cx="41" cy="12" r="8" stroke="var(--blue)"/><path d="M37 12l3 3 5-6"/></svg>
  <span class="num">02</span><h3>Handle The<br>Budgeting Process</h3>
  <p>Lorem ipsum dolor sit amet, consetetur sadipscing elitr, sed diam nonumy eirmod tempor invidunt ut labore et dolore magna aliquyam erat...</p>
</div>
<div class="service-card" style="left:762px">
  <svg width="54" height="54" viewBox="0 0 54 54" fill="none" stroke="#1b2430" stroke-width="2"><circle cx="16" cy="26" r="10"/><circle cx="16" cy="26" r="4" stroke="var(--blue)"/><circle cx="40" cy="10" r="5" stroke="var(--blue)"/><path d="M32 24h16v10H32zM34 40h12l-6 10z"/></svg>
  <span class="num">03</span><h3>Provide<br>Temporary Staffing.</h3>
  <p>Lorem ipsum dolor sit amet, consetetur sadipscing elitr, sed diam nonumy eirmod tempor invidunt ut labore et dolore magna aliquyam erat...</p>
</div>

<!-- Reviews -->
<div class="eyebrow center" style="top:1815px">Client Reviews</div>
<h2 class="abs sec-title center" style="top:1832px">What Our Clients say</h2>
<div class="rule" style="left:580px;top:1880px"></div>
<p class="abs center" style="top:1900px;font-size:12px;line-height:24px;color:#3d4650">Lorem ipsum dolor sit amet, consetetur sadipscing elitr, sed diam nonumy eirmod<br>ipsum dolor sit amet, consetetur sadipscing elitr, sed diam nonumy...</p>
<div class="arrow-box" style="left:956px;background:#edf0f3">&larr;</div>
<div class="arrow-box" style="left:1000px;background:var(--blue);color:var(--white)">&rarr;</div>

<div class="review-card" style="left:-140px;top:1930px;opacity:.8">
  <span class="quote">&rdquo;</span>
</div>
<div class="review-card" style="left:161px;top:1976px">
  <span class="avatar" role="img" aria-label="Client portrait"></span><span class="quote">&rdquo;</span>
  <p>Lorem ipsum dolor sit amet, consetetur sadipscing elitr, sed diam nonumy eirmod tempor invidunt ut labore et dolore...</p>
  <span class="by">– Lorem ipsum dolor sit</span><span class="stars">★★★★<span>★</span></span>
</div>
<div class="review-card" style="left:461px;top:1996px">
  <span class="avatar" role="img" aria-label="Client portrait"></span><span class="quote">&rdquo;</span>
  <p>Lorem ipsum dolor sit amet, consetetur sadipscing elitr, sed diam nonumy eirmod tempor invidunt ut labore et dolore...</p>
  <span class="by">– Lorem ipsum dolor sit</span><span class="stars">★★★★<span>★</span></span>
</div>
<div class="review-card" style="left:762px;top:1976px">
  <span class="avatar" role="img" aria-label="Client portrait"></span><span class="quote">&rdquo;</span>
  <p>Lorem ipsum dolor sit amet, consetetur sadipscing elitr, sed diam nonumy eirmod tempor invidunt ut labore et dolore...</p>
  <span class="by">– Lorem ipsum dolor sit</span><span class="stars">★★★★<span>★</span></span>
</div>
<div class="review-card" style="left:1056px;top:1937px;opacity:.8">
  <span class="avatar" role="img" aria-label="Client portrait"></span>
  <p style="width:140px;overflow:hidden;white-space:nowrap;color:var(--muted)">Lorem ipsum dolor sit<br>consetetur sadipscing<br>nonumy eirmod tempor<br>labore et dolore...</p>
  <span class="by">– Lorem ipsum dolor</span><span class="stars">★★★★<span>★</span></span>
</div>

<!-- Blogs -->
<div class="abs blogs-bg"></div>
<h2 class="abs sec-title center" style="top:2406px">Our Latest Blogs</h2>
<div class="rule" style="left:580px;top:2458px"></div>

<article class="blog" style="left:161px">
  <div class="img" role="img" aria-label="Hands writing notes beside a laptop and glasses" style="background:linear-gradient(135deg,#e8d9b8,#c2b79f 50%,#8c8a84)"></div>
  <h3>Lorem ipsum dolor sit amet, co setetur sadipscing elit...</h3>
  <p>Lorem Ipsum is simply dummy text of the prin ting and typesetting industry Lorem Ipsum has been the industry.</p>
  <div class="author"><i role="img" aria-label="Author portrait"></i><div><b>Lorem ipsum dolor sit</b><small>Ipsum Lorem simply....</small></div></div>
</article>
<article class="blog" style="left:463px">
  <div class="img" role="img" aria-label="Presenter explaining charts in a meeting room" style="background:linear-gradient(135deg,#e9ecef,#b8c0c8 55%,#59606a)"></div>
  <h3>Lorem ipsum dolor sit amet, co setetur sadipscing elit...</h3>
  <p>Lorem Ipsum is simply dummy text of the prin ting and typesetting industry Lorem Ipsum has been the industry.</p>
  <div class="author"><i role="img" aria-label="Author portrait"></i><div><b>Lorem ipsum dolor sit</b><small>Ipsum Lorem simply....</small></div></div>
</article>
<article class="blog" style="left:767px">
  <div class="img" role="img" aria-label="Stacked coins with a rising blue growth graph" style="background:linear-gradient(160deg,#0d3d8c,#1f6fd1 55%,#b88a4a)"></div>
  <h3>Lorem ipsum dolor sit amet, co setetur sadipscing elit...</h3>
  <p>Lorem Ipsum is simply dummy text of the prin ting and typesetting industry Lorem Ipsum has been the industry.</p>
  <div class="author"><i role="img" aria-label="Author portrait"></i><div><b>Lorem ipsum dolor sit</b><small>Ipsum Lorem simply....</small></div></div>
</article>
<div class="btn" style="left:540px;top:2911px;width:112px;height:37px">View All</div>

<!-- Footer -->
<footer class="abs footer">
  <div class="abs logo" style="left:161px;top:66px"><span class="mark"></span><span class="name">KELVANE</span></div>
  <p class="abs footer-about">Lorem Ipsum is simply dummy text of the prin ting and typesetting industry Lorem Ipsum has been the industry.Lorem Ipsum is of the prin ting and typesetting industry Lorem Ipsum has been the industry.</p>
  <span class="social" style="left:161px"></span>
  <span class="social" style="left:207px"></span>
  <span class="social" style="left:253px"></span>
  <span class="social" style="left:300px"></span>
  <span class="social" style="left:346px"></span>

  <span class="fhead" style="left:495px">Contact</span>
  <svg class="abs" style="left:495px;top:180px" width="14" height="18" viewBox="0 0 14 18" fill="none" stroke="var(--blue)" stroke-width="1.3"><path d="M7 17s6-6 6-10A6 6 0 0 0 1 7c0 4 6 10 6 10z"/><circle cx="7" cy="7" r="2"/></svg>
  <span class="fitem" style="left:527px;top:181px">48 Harlow Avenue<br>Austin, USA</span>
  <svg class="abs" style="left:495px;top:228px" width="16" height="16" viewBox="0 0 16 16" fill="none" stroke="var(--blue)" stroke-width="1.3"><path d="M3 1l3 3-2 2c1 2 4 5 6 6l2-2 3 3-2 2C7 15 1 9 1 3z"/></svg>
  <span class="fitem" style="left:527px;top:228px">1-555-014-2290</span>
  <svg class="abs" style="left:495px;top:272px" width="16" height="12" viewBox="0 0 16 12" fill="none" stroke="var(--blue)" stroke-width="1.3"><rect x="1" y="1" width="14" height="10"/><path d="M1 1l7 6 7-6"/></svg>
  <span class="fitem" style="left:527px;top:271px">info@kelvane-consult.com</span>

  <span class="fhead" style="left:690px">Links</span>
  <span class="fitem" style="left:692px;top:146px">Home</span>
  <span class="fitem" style="left:692px;top:175px">About Us</span>
  <span class="fitem" style="left:692px;top:204px">Services</span>
  <span class="fitem" style="left:692px;top:233px">Contact Us</span>

  <span class="fhead" style="left:812px">Subscribe</span>
  <span class="fitem" style="left:812px;top:148px;width:230px;font-size:12px;line-height:19px">Subscribe to our newsletter to get our latest update &amp; news.</span>
  <div class="abs subscribe-box">Your email</div>
  <div class="abs send"><svg width="18" height="18" viewBox="0 0 18 18" fill="none" stroke="#fff" stroke-width="1.4"><path d="M1 8l16-7-6 16-3-6z M8 11l9-10"/></svg></div>

  <p class="abs copy">© 2023 Kelvane Consulting. All Rights Reserved.</p>
</footer>

</body>
</html>
```